BKA

Please send us some options for letterhead I attached our Logo. In addition to the Logo we need this information somewhere on the page

47 Fenbury Lane
Milbrook, ME 04127
203-481-7629

```html
<!DOCTYPE html>
<html lang="en">
<head>
<meta charset="utf-8">
<title>BKA Letterhead</title>
<link rel="stylesheet" href="https://fonts.googleapis.com/css2?family=Cabin:wght@500;600&display=swap">
<style>
  :root {
    --paper: #ffffff;
    --brand-navy: #253f94;
    --brand-blue: #4a79b4;
    --frame-blue: #4d7ab6;
    --ink-light: #ffffff;
  }
  html, body {
    margin: 0;
    padding: 0;
    overflow: hidden;
    background: var(--paper);
  }
  .letterhead {
    position: relative;
    width: 927px;
    height: 1200px;
    background: var(--paper);
    overflow: hidden;
    font-family: "Cabin", "Candara", sans-serif;
  }
  .sidebar {
    position: absolute;
    left: 750px;
    top: 210px;
    width: 136px;
    height: 987px;
  }
  .sidebar__stripe {
    position: absolute;
    top: 0;
    bottom: 0;
    background: var(--brand-blue);
  }
  .sidebar__stripe--left { left: 0; width: 65px; }
  .sidebar__stripe--center { left: 68px; width: 2px; }
  .sidebar__stripe--right { left: 73px; width: 63px; }
  .brand-block {
    position: absolute;
    left: 730px;
    top: 103px;
    width: 174px;
    height: 121px;
    box-sizing: border-box;
    background: var(--paper);
    border: 4px solid var(--frame-blue);
    padding: 4px;
  }
  .brand-block__inner {
    width: 100%;
    height: 100%;
    background: var(--brand-navy);
    color: var(--ink-light);
    text-align: center;
    box-sizing: border-box;
    padding-top: 6px;
  }
  .brand-block__name {
    margin: 0;
    font-size: 35px;
    font-weight: 500;
    line-height: 38px;
    letter-spacing: 1px;
  }
  .brand-block__address {
    margin: 1px 0 0;
    font-style: normal;
    font-size: 12.5px;
    font-weight: 600;
    line-height: 15px;
  }
</style>
</head>
<body>
  <main class="letterhead">
    <div class="sidebar" aria-hidden="true">
      <div class="sidebar__stripe sidebar__stripe--left"></div>
      <div class="sidebar__stripe sidebar__stripe--center"></div>
      <div class="sidebar__stripe sidebar__stripe--right"></div>
    </div>
    <header class="brand-block">
      <div class="brand-block__inner">
        <h1 class="brand-block__name">BKA</h1>
        <address class="brand-block__address">
          47 Fenbury Lane<br>
          Milbrook, ME 04127<br>
          203-481-7629
        </address>
      </div>
    </header>
  </main>
</body>
</html>
```